AVOID HOT “HARISSA” SAUCE. IN CAN

Brand Overview: Create a dynamic and eye-catching label for our new hot sauce IN CAN, “DUMEL.” Our brand is all about delivering a fiery flavor experience that combines the intensity of various peppers with unique, bold ingredients. The hot sauce targets spice enthusiasts who crave both heat and distinctive taste profiles.

Key Messages: Intensity: Emphasize the extreme heat level of the hot sauce to appeal to spice lovers.
Traditional: The taste is traditional
Flavor Fusion: Highlight the unique blend of peppers and special ingredients that sets DUMEL

Quality Ingredients: Convey the use of premium, natural ingredients to reinforce the high-quality aspect of our product.

Versatility: Communicate the sauce's versatility – perfect for various cuisines and dishes. Design Elements:

Color Palette: Use fiery reds, oranges, and yellows to convey the heat, with accents of dark and smoky tones to suggest depth of flavor.

Typography: Choose bold and legible fonts for the product name, ensuring it is easily readable from a distance.
Imagery: Incorporate visuals of flaming peppers or a stylized fire to reinforce the spicy nature of the hot sauce.
Consider using images of the key ingredients to showcase the fusion of flavors.

Texture/Background: Add a textured or gradient background to enhance visual interest and give a sense of depth.

Label Information: Product Name Hot Sauce "HARISSA" Heat Level

Indicator: Use a visual scale or iconography to indicate the spiciness level.

Ingredients: Highlight key ingredients and emphasize their quality, peppers, water, salt
SIZE: L: 12cm H: 5.5cm

Net Weight: 140g

Regulatory Information: Ensure compliance with all relevant food labeling regulations, including ingredients list, nutritional information, and contact details.

Competitor Analysis: Examine other hot sauce labels in the market to identify design trends and differentiators.
Inspiration: Consider drawing inspiration from elements like flames, peppers, or global spice motifs to create a visually striking and memorable label. Mood/Emotion: The label should evoke excitement, daring, and a sense of adventure – capturing the thrill of experiencing the intense flavor of HARISSA DUMEL Hot Sauce.

Target Audience: Spice enthusiasts, foodies, and individuals seeking a unique and bold addition to their culinary experiences.

Delivery Format: The label design should be suitable for various packaging sizes, ensuring scalability without sacrificing visual impact. Remember to balance the vibrant and intense visuals with clarity and readability and send the FONT at the moment of the delivery.
Updates

Need extra days to review

Target Market(s)

European

Font styles to use
Decorative

Colors
FFF300
FFF600
FEFA6F
FFFEC7
FFFEE8
FFC000
F8CF3A
FAE287
FDF2CF
FEFAEE
EE7325
F08F49
F5BC92
FAE3D3
FDF4ED
EB3D1F
EC4F4E
F09395
F8D3D4
FCEDEE

Requirements
Must have
• LOGO, BARCODE, Nutritional facts, INGREDIENTS

```html
<!DOCTYPE html>
<html lang="en">
<head>
<meta charset="utf-8">
<title>HARISSA Hot Sauce – DUMEL can labels</title>
<link rel="stylesheet" href="https://fonts.googleapis.com/css2?family=Montserrat:wght@400;500;700;800&family=Roboto+Condensed:wght@400;700&display=swap">
<style>
:root{
  --paper:#fdf4dc;
  --cream:#fdf2cf;
  --label-red:#7a0a06;
  --label-deep:#5c0303;
  --maroon:#5a1f22;
  --orange:#ee7325;
  --amber:#ffc000;
  --gold:#f8cf3a;
  --flame-red:#eb3d1f;
  --white:#ffffff;
  --ink:#1b1b1b;
}
*{box-sizing:border-box;margin:0;padding:0}
html,body{width:1200px;height:1200px;overflow:hidden}
body{background:var(--paper);font-family:"Montserrat",sans-serif;position:relative}

.label{position:absolute;overflow:hidden;background:var(--label-red)}
.label--flame{left:107px;top:94px;width:981px;height:445px}
.label--badge{left:114px;top:670px;width:972px;height:442px;background:linear-gradient(90deg,#741008 0%,var(--label-deep) 45%,#6a0604 100%)}

.pepper-field{position:absolute;inset:0 0 45% 0;
  background:radial-gradient(ellipse at 20% 40%,rgba(170,20,18,.55),rgba(170,20,18,0) 40%),
             radial-gradient(ellipse at 78% 35%,rgba(170,20,18,.55),rgba(170,20,18,0) 40%)}
.fire-band{position:absolute;left:0;right:0;bottom:0;height:48%;
  background:linear-gradient(180deg,rgba(190,20,10,0) 0%,rgba(200,30,12,.55) 45%,rgba(235,61,31,.8) 80%,rgba(240,140,40,.85) 100%)}
.hero-pepper{position:absolute;border-radius:45% 45% 40% 40%;
  background:radial-gradient(ellipse at 50% 70%,#ffc000 0%,#f08f49 25%,#eb3d1f 55%,rgba(180,20,10,0) 78%)}
.label--flame .hero-pepper{left:371px;top:258px;width:230px;height:187px}
.label--badge .hero-pepper{left:361px;top:222px;width:262px;height:220px}
.glow{position:absolute;left:0;top:0;right:0;height:60%;
  background:radial-gradient(ellipse at 60% 70%,rgba(140,30,18,.55),rgba(140,30,18,0) 45%)}

.side-copy{position:absolute;color:var(--white);width:250px}
.label--flame .side-copy{left:18px;top:68px}
.label--badge .side-copy{left:10px;top:228px}
.side-copy h3{font-weight:700;font-size:10.5px;letter-spacing:.2px;margin-bottom:6px}
.side-copy p{font-weight:400;font-size:9.6px;line-height:12.4px;letter-spacing:.6px}
.side-copy hr{border:0;border-top:1px solid rgba(255,255,255,.85);width:235px;margin:10px 0 8px}

.brand{position:absolute;display:flex;align-items:center;gap:4px;color:var(--cream);font-weight:800;letter-spacing:.5px}
.brand i{display:block;border-radius:50%;background:var(--gold)}
.label--flame .brand{right:22px;top:38px;font-size:18px}
.label--flame .brand i{width:8px;height:8px}
.label--badge .brand{right:24px;top:22px;font-size:14px}
.label--badge .brand i{width:6px;height:6px}

/* flame label title panel */
.title-panel{position:absolute;left:393px;top:13px;width:175px;height:247px;
  background:var(--orange);border:2px solid var(--flame-red);border-radius:10px;padding:9px}
.title-panel .inner{position:relative;width:100%;height:100%;background:var(--maroon);
  border:1px solid var(--flame-red);border-radius:4px;text-align:center;color:var(--white)}
.title-panel .kicker{position:absolute;top:22px;width:100%;font-size:14px;font-weight:400;letter-spacing:.3px}
.title-panel .name{position:absolute;top:40px;width:100%;font-size:25px;font-weight:800;color:var(--amber);letter-spacing:.3px}
.title-panel .level{position:absolute;top:77px;width:100%;font-size:14px;font-weight:400}
.title-panel .motto{position:absolute;top:106px;width:100%;font-size:15px;font-weight:800;line-height:20.5px}
.title-panel .rule{position:absolute;top:195px;left:34px;right:34px;border-top:1px solid var(--white)}

/* badge label title panel */
.name-panel{position:absolute;left:383px;top:50px;width:207px;height:149px;
  background:var(--cream);border:2px solid var(--flame-red);border-radius:14px;padding:9px}
.name-panel .inner{position:relative;width:100%;height:100%;background:var(--maroon);
  border-radius:8px;text-align:center;color:var(--cream)}
.name-panel .kicker{position:absolute;top:22px;width:100%;font-size:12.5px;font-weight:400}
.name-panel .name{position:absolute;top:39px;width:100%;font-size:31px;font-weight:800;letter-spacing:.5px}
.name-panel .level{position:absolute;top:86px;width:100%;font-size:12.5px;font-weight:400}
.name-panel .line{position:absolute;left:52px;right:52px;border-top:1px solid var(--cream)}
.tagline{position:absolute;left:300px;top:212px;width:372px;text-align:center;color:var(--cream);font-weight:800;font-size:13.5px;letter-spacing:.3px}

/* nutrition table */
.nutrition{position:absolute;background:var(--white);color:var(--ink);font-family:"Roboto Condensed",sans-serif;padding:4px 3px;border:1px solid #ccc;overflow:hidden}
.label--flame .nutrition{left:838px;top:236px;width:130px;height:200px;font-size:5.1px}
.label--badge .nutrition{left:824px;top:218px;width:139px;height:214px;font-size:5.5px}
.nutrition .title{font-size:1.65em;line-height:1.25em;font-weight:500}
.nutrition .per{line-height:1.45em}
.nutrition .head{display:flex;justify-content:space-between;font-size:.72em;line-height:1.3em;border-top:3px solid var(--ink);margin-top:2px;padding-top:2px;font-weight:700}
.nutrition .row{display:flex;justify-content:space-between;line-height:1.45em;border-top:.5px solid #666}
.nutrition .row.indent span:first-child{padding-left:.6em}
.nutrition .row.thick{border-top:1.5px solid var(--ink)}
.nutrition b{font-weight:700}
.nutrition .note{border-top:2px solid var(--ink);line-height:1.45em;padding-top:1px}
.nutrition .tiny{font-size:.68em;line-height:1.3em;font-weight:700}
.nutrition .ingr{border-top:.5px solid #666;line-height:1.45em}
</style>
</head>
<body>

<section class="label label--flame">
  <div class="pepper-field" role="img" aria-label="Scattered red chili peppers"></div>
  <div class="fire-band" role="img" aria-label="Stylized fire flames along the bottom of the label"></div>
  <div class="hero-pepper" role="img" aria-label="Red chili pepper engulfed in flames"></div>

  <div class="side-copy">
    <h3>QUALITY INGREDIENTS:</h3>
    <p>&nbsp;Convey the use of premium,<br>natural ingredients to reinforce<br>&nbsp;the high-quality aspect of our product.</p>
    <hr>
    <p>Emphasize the extreme heat level of the hot sauce to appeal to spice lovers.</p>
  </div>

  <div class="title-panel">
    <div class="inner">
      <div class="kicker">HOT SAUCE</div>
      <div class="name">HARISSA</div>
      <div class="level">HEAT LEVEL</div>
      <div class="motto">THE<br>TASTE<br>IS<br>TRADITIONAL</div>
      <div class="rule"></div>
    </div>
  </div>

  <div class="brand"><i></i>DUMEL</div>

  <div class="nutrition">
    <div class="title">Nutritional Facts<br>Valeur nutritive</div>
    <div class="per">Per 1 tbsp (15 ml) / Portion 15 ml<br>Servings per 375 ml container: 25</div>
    <div class="head"><span>Amount<br>Teneur par portion</span><span style="text-align:right">% Daily Value*<br>% valeur quotidienne*</span></div>
    <div class="row thick"><span><b>Calories / Calories</b> 120</span><span></span></div>
    <div class="row"><span><b>Fat / Lipides</b> 14 g</span><b>22 %</b></div>
    <div class="row indent"><span>Saturated / saturés 2 g</span><b>10 %</b></div>
    <div class="row indent"><span>Trans / Trans 0 g</span><span></span></div>
    <div class="row indent"><span>Polyunsaturated / Polyinsaturés 1 g</span><span></span></div>
    <div class="row indent"><span>Monounsaturated / Monoinsaturés 10 g</span><span></span></div>
    <div class="row"><span><b>Protein / Protéines</b> 0 g</span><b>0 %</b></div>
    <div class="row"><span><b>Sodium / Sodium</b> 0 mg</span><b>0 %</b></div>
    <div class="row"><span><b>Carbohydrate / Glucides</b> 0 g</span><b>0 %</b></div>
    <div class="row indent"><span>Fibre / Fibres 0 g</span><b>0 %</b></div>
    <div class="row indent"><span>Sugar / Sucres 0 g</span><span></span></div>
    <div class="note">Not a significant source of other nutrients.<br>Source négligeable d'autres éléments nutritifs.</div>
    <div class="tiny">*Percent Daily Values are based on a 2,000 calorie diet. Pourcentage de valeurs quotidiennes sont basés sur un régime de 2,000 calories.</div>
    <div class="ingr">Ingredients: Extra Virgin Olive Oil, natural flavours.<br>Ingrédients: Huile d'olive extra vierge, ingrédients naturels.</div>
  </div>
</section>

<section class="label label--badge">
  <div class="glow"></div>
  <div class="fire-band" role="img" aria-label="Stylized fire flames along the bottom of the label"></div>
  <div class="hero-pepper" role="img" aria-label="Red chili pepper engulfed in flames"></div>

  <div class="name-panel">
    <div class="inner">
      <div class="kicker">HOT SAUCE</div>
      <div class="line" style="top:38px"></div>
      <div class="name">HARISSA</div>
      <div class="line" style="top:84px"></div>
      <div class="level">HEAT LEVEL</div>
    </div>
  </div>
  <div class="tagline">THE TASTE IS TRADITIONAL</div>

  <div class="side-copy">
    <h3>QUALITY INGREDIENTS:</h3>
    <p>&nbsp;Convey the use of premium,<br>natural ingredients to reinforce<br>&nbsp;the high-quality aspect of our product.</p>
    <hr>
    <p>Emphasize the extreme heat level of the hot sauce to appeal to spice lovers.</p>
  </div>

  <div class="brand"><i></i>DUMEL</div>

  <div class="nutrition">
    <div class="title">Nutritional Facts<br>Valeur nutritive</div>
    <div class="per">Per 1 tbsp (15 ml) / Portion 15 ml<br>Servings per 375 ml container: 25</div>
    <div class="head"><span>Amount<br>Teneur par portion</span><span style="text-align:right">% Daily Value*<br>% valeur quotidienne*</span></div>
    <div class="row thick"><span><b>Calories / Calories</b> 120</span><span></span></div>
    <div class="row"><span><b>Fat / Lipides</b> 14 g</span><b>22 %</b></div>
    <div class="row indent"><span>Saturated / saturés 2 g</span><b>10 %</b></div>
    <div class="row indent"><span>Trans / Trans 0 g</span><span></span></div>
    <div class="row indent"><span>Polyunsaturated / Polyinsaturés 1 g</span><span></span></div>
    <div class="row indent"><span>Monounsaturated / Monoinsaturés 10 g</span><span></span></div>
    <div class="row"><span><b>Protein / Protéines</b> 0 g</span><b>0 %</b></div>
    <div class="row"><span><b>Sodium / Sodium</b> 0 mg</span><b>0 %</b></div>
    <div class="row"><span><b>Carbohydrate / Glucides</b> 0 g</span><b>0 %</b></div>
    <div class="row indent"><span>Fibre / Fibres 0 g</span><b>0 %</b></div>
    <div class="row indent"><span>Sugar / Sucres 0 g</span><span></span></div>
    <div class="note">Not a significant source of other nutrients.<br>Source négligeable d'autres éléments nutritifs.</div>
    <div class="tiny">*Percent Daily Values are based on a 2,000 calorie diet. Pourcentage de valeurs quotidiennes sont basés sur un régime de 2,000 calories.</div>
    <div class="ingr">Ingredients: Extra Virgin Olive Oil, natural flavours.<br>Ingrédients: Huile d'olive extra vierge, ingrédients naturels.</div>
  </div>
</section>

</body>
</html>
```